依頼概要
・依頼の目的/概要
人生100年時代に、認知症や介護予防・改善に役立つ、化粧療法レクレーションの表紙デザインをお願いします。

・本の内容
高齢者の皆さんを抱えた、娘さん世代、ソーシャルビジネスとして取り組みたい女性、人の役に立ちたい・介護や医療関係者のスキルアップとして、心を癒すスキンタッチケアとしての化粧療法レクレーションを知って頂き、その効果を実例等で理解する事で、実践してみたくなる内容にしています。またお仕事としても、ボランティアとしても活躍できるセラピストの役割や募集にもふれています。
化粧療法レクレーションがどんなものか?!やるとどんな効果がきたいできるのか?!に、研究データーと実際の実例を交えて説明・解説した本です。

・デザイン要望
美容で心が癒される事が、伝わるようなイメージと解説でもあるので、化粧療法レクレーションのバイブルみたいな感じでしょうか?!(イメージカラーは、ピンクです。http://tkvb.or.jp tkvb-sora.com 色の感じです、参考資料)
もちろん、デザイナーさんのセンスにお任せします。

その他何かご不明な点がございましたら、お気軽にご質問ください。
よろしくお願いいたします。
■ 選んだ理由

認知症や介護の予防・改善を目指した療法ですので、見た方が、明るく安心し、そして楽しみになるイメージが持てるデザインを選びました。特に当選したものは、高齢者と若者が一緒に映る写真の印象が、表題のレクレーションのイメージに繋がるということが、一番の選定理由です。

■ 提案者全員のお礼・コメント

素晴らしい表紙のデザインの応募をいただき、本当に感謝しています。
選定は、本当に悩みました。いくつも表紙にしたい作品がありました。出して頂いた作品が、教科書的と、読み物的な提案を頂いたように思います。皆さん素晴らしかったのですが、今回は親しみやすさを重視させて頂きました。特に最初に応募して頂いた、pelmiさんの表紙には、私の言いたい事が網羅されていて、良かったです。が、今回のテーマを考えて、残念ながら選定致しませんでした。
次の機会に皆様とお仕事ができれば、嬉しいです。ありがとうございました。

```html
<!DOCTYPE html>
<html lang="ja">
<head>
<meta charset="utf-8">
<title>化粧療法レクレーション</title>
<link href="https://fonts.googleapis.com/css2?family=Noto+Serif+JP:wght@500;700;900&display=swap" rel="stylesheet">
<style>
  :root {
    --paper: #fdf8f8;
    --rose: #e2497c;
    --rose-deep: #c92f63;
    --rose-soft: #f2b7c6;
    --blush: #f7d6de;
    --band-top: #fbe6ea;
    --band-bottom: #ef9fb2;
    --ink: #4a3438;
    --lilac: #c9b6d6;
  }
  * { margin: 0; padding: 0; box-sizing: border-box; }
  html, body { width: 751px; height: 1200px; overflow: hidden; background: var(--paper); }
  .cover {
    position: relative;
    width: 751px; height: 1200px;
    background: var(--paper);
    font-family: "Noto Serif JP", serif;
    color: var(--ink);
    overflow: hidden;
  }
  .wreath {
    position: absolute;
    left: 40px; top: 40px;
    width: 660px; height: 740px;
    border-radius: 50%;
    background: radial-gradient(ellipse at center, rgba(253,248,248,0) 56%, var(--blush) 63%, var(--rose-soft) 68%, var(--lilac) 71%, rgba(253,248,248,0) 72%);
  }
  .heading { position: absolute; left: 0; width: 100%; text-align: center; line-height: 1; }
  .lead { top: 160px; font-size: 36px; font-weight: 700; color: var(--ink); letter-spacing: 2px; }
  .lead-accent { top: 222px; font-size: 38px; font-weight: 700; color: var(--rose); letter-spacing: 2px; }
  .title-main {
    top: 282px; font-size: 88px; font-weight: 900; color: var(--rose);
    letter-spacing: 4px;
  }
  .title-sub {
    top: 400px; font-size: 66px; font-weight: 900; color: var(--rose);
    letter-spacing: 0;
  }
  .author {
    position: absolute; left: 220px; top: 520px;
    font-size: 38px; font-weight: 700; color: var(--ink); letter-spacing: 6px; line-height: 1;
  }
  .tagline {
    position: absolute; left: 62px; top: 655px;
    font-size: 32px; font-weight: 700; color: var(--rose); letter-spacing: 0; line-height: 1;
  }
  .band {
    position: absolute; left: 0; top: 862px;
    width: 751px; height: 338px;
    background: linear-gradient(180deg, var(--band-top), var(--band-bottom));
  }
  .figure {
    position: absolute; left: 455px; top: 470px;
    width: 240px; height: 392px;
    border-radius: 120px 120px 0 0;
    background: linear-gradient(180deg, #f3dccf 0%, #e8c2c9 55%, #b79ac9 100%);
  }
  .promise {
    position: absolute; left: 0; top: 915px;
    width: 751px;
    text-align: center;
  }
  .promise-line {
    display: block;
    font-size: 62px; font-weight: 900; color: var(--ink);
    line-height: 1.9; letter-spacing: 2px;
  }
  .promise-em { color: var(--rose-deep); }
  .promise-num { color: var(--rose-deep); font-size: 74px; }
</style>
</head>
<body>
  <main class="cover">
    <div class="wreath" role="img" aria-label="ピンクの薔薇と葉、三日月と星で囲んだ円形の花のリース"></div>

    <p class="heading lead">心を癒し、</p>
    <p class="heading lead-accent">健康寿命を延ばす</p>
    <h1 class="heading title-main">化粧療法</h1>
    <h2 class="heading title-sub">レクレーション</h2>
    <p class="author">森 佳奈子</p>

    <p class="tagline">明るく・元気に・美しく</p>

    <div class="band"></div>
    <div class="figure" role="img" aria-label="頬に手を添えて微笑む女性のイラスト"></div>

    <section class="promise">
      <span class="promise-line"><span class="promise-num">60</span>分間で<span class="promise-em">お肌</span>も<span class="promise-em">心</span>も</span>
      <span class="promise-line">綺麗になるメソッド</span>
    </section>
  </main>
</body>
</html>
```